Business Card Design needed for logo design project

Would like a professional business card for a company involved in financial and latest technologies including CAD design. We would like the card to convey professionalism and communicate that we are involved in up to date technology solutions.

Target Market(s)

Business 2 Business sales

Industry/Entity Type

Financial

Colors

Designer to choose colors to be used in the design.

Requirements
Must have
• Business Name
Logo
Name
Phone
Email
Nice to have
• Website

```html
<!DOCTYPE html>
<html lang="en">
<head>
<meta charset="utf-8">
<title>ZELMORAN Business Card</title>
<link rel="stylesheet" href="https://fonts.googleapis.com/css2?family=Open+Sans:wght@400;800&display=swap">
<style>
  :root {
    --brand-red: #d8222a;
    --brand-navy: #1c2150;
    --paper: #ffffff;
    --backdrop: #e6e7ea;
    --card-shadow: rgba(0, 0, 0, 0.18);
  }
  * { margin: 0; padding: 0; box-sizing: border-box; }
  html, body {
    width: 1200px;
    height: 736px;
    overflow: hidden;
    background: var(--backdrop);
    font-family: "Open Sans", Arial, sans-serif;
  }
  .sheet {
    width: 1200px;
    height: 736px;
    display: flex;
    align-items: center;
    justify-content: center;
    gap: 40px;
  }
  .card {
    position: relative;
    width: 520px;
    height: 300px;
    overflow: hidden;
    box-shadow: 0 6px 18px var(--card-shadow);
  }
  .card--front { background: var(--brand-red); }
  .card--back { background: var(--paper); }

  .wordmark {
    position: absolute;
    font-weight: 800;
    letter-spacing: 1px;
    line-height: 1;
    white-space: nowrap;
  }
  .card--front .wordmark {
    left: 60px;
    top: 118px;
    font-size: 52px;
    color: var(--paper);
  }
  .card--back .wordmark {
    left: 20px;
    top: 114px;
    font-size: 34px;
    color: var(--brand-navy);
  }
  .band {
    position: absolute;
    display: block;
  }
  .card--front .band--top {
    right: 0; bottom: 62px;
    width: 240px; height: 10px;
    background: var(--brand-navy);
  }
  .card--front .band--bottom {
    right: 0; bottom: 46px;
    width: 240px; height: 10px;
    background: var(--paper);
  }
  .card--back .band--top {
    left: 0; top: 162px;
    width: 270px; height: 9px;
    background: var(--brand-navy);
  }
  .card--back .band--bottom {
    left: 0; top: 176px;
    width: 270px; height: 9px;
    background: var(--brand-red);
  }
  .contact {
    position: absolute;
    right: 28px;
    top: 100px;
    text-align: right;
    color: var(--brand-navy);
    font-size: 14px;
    line-height: 20px;
    list-style: none;
  }
</style>
</head>
<body>
<main class="sheet">
  <section class="card card--front" aria-label="Business card front">
    <span class="wordmark">ZELMORAN</span>
    <span class="band band--top" aria-hidden="true"></span>
    <span class="band band--bottom" aria-hidden="true"></span>
  </section>

  <section class="card card--back" aria-label="Business card back">
    <span class="wordmark">ZELMORAN</span>
    <span class="band band--top" aria-hidden="true"></span>
    <span class="band band--bottom" aria-hidden="true"></span>
    <ul class="contact">
      <li class="contact__name">NAME</li>
      <li class="contact__title">Sales Manager</li>
      <li class="contact__phone">+41987654321</li>
      <li class="contact__email">hello@zelmoran-fin.com</li>
      <li class="contact__web">www.zelmoran-fin.com</li>
    </ul>
  </section>
</main>
</body>
</html>
```